Stationery design for Covenant Elders Assembly
Covenant Elders Assembly of Harvest Fellowship
Stationery design for Covenant Elders Assembly - Religion and Spirituality
Creative Brief
Professional
Rev. Tobias Okonkwe
Convener/Chairman Board of Trustees
14 Rimi Kasa Street, off Gwagwa - Karu Link Road, Nyanya Abuja, FCT, Nigeria
covenant.elders.assembly@mailvale.example
tundrivex tundrivex
Please include design for letterhead and envelopes
Please include design for stationery too
Please let us have the full name of the entity indicated on the card either on the front like a footnote or behind. This is the full name: Covenant Elders Assembly of Harvest Fellowship Thanks

```html
<!DOCTYPE html>
<html lang="en">
<head>
<meta charset="utf-8">
<title>Covenant Elders Assembly – Business Card</title>
<link rel="stylesheet" href="https://fonts.googleapis.com/css2?family=Arimo:wght@400;700&family=Tinos:wght@400;700&display=swap">
<style>
  :root {
    --canvas: #e9e9ec;
    --card-dark: #1c1c1e;
    --card-light: #ffffff;
    --brand-blue: #2f5fb3;
    --brand-orange: #f08a1c;
    --brand-red: #e2452b;
    --brand-yellow: #f5b51c;
    --brand-purple: #5a3aa8;
    --ink: #333338;
    --ink-soft: #6b6b72;
    --rule: #cfcfd6;
  }
  * { margin: 0; padding: 0; box-sizing: border-box; }
  html, body { width: 1200px; height: 914px; overflow: hidden; }
  body {
    background: var(--canvas);
    display: flex;
    flex-direction: column;
    align-items: center;
    justify-content: center;
    gap: 34px;
    font-family: "Arimo", Arial, sans-serif;
  }
  .card {
    position: relative;
    width: 720px;
    height: 400px;
    border-radius: 14px;
    overflow: hidden;
    box-shadow: 0 6px 18px rgba(0,0,0,.12);
  }

  /* Brand lockup */
  .brand-lockup { display: flex; align-items: center; gap: 14px; }
  .brand-mark {
    width: 52px; height: 52px; border-radius: 50%;
    background: var(--brand-orange);
    flex: none;
  }
  .brand-name {
    font-weight: 400;
    font-size: 24px;
    line-height: 1.1;
    color: var(--brand-orange);
  }

  /* Back side */
  .card-back { background: var(--card-dark); }
  .card-back .brand-lockup {
    position: absolute; left: 50%; top: 50%;
    transform: translate(-50%, -50%);
  }
  .card-back .edge-band {
    position: absolute; left: 0; right: 0; bottom: 0; height: 10px;
    background: var(--brand-yellow);
  }

  /* Front side */
  .card-front { background: var(--card-light); }
  .card-front .brand-lockup {
    position: absolute; left: 56px; top: 150px;
  }
  .card-front .brand-name { color: var(--brand-blue); font-size: 26px; }
  .divider {
    position: absolute; left: 318px; top: 56px; width: 2px; height: 230px;
    background: var(--brand-blue);
  }
  .contact {
    position: absolute; left: 338px; top: 56px; right: 34px;
    font-family: "Tinos", "Times New Roman", serif;
    color: var(--ink);
  }
  .contact .name {
    font-weight: 700; font-size: 24px; color: var(--brand-blue);
    border-bottom: 1px solid var(--rule); padding-bottom: 6px;
  }
  .contact .role { font-size: 14px; color: var(--ink-soft); margin-top: 6px; }
  .contact .address { font-size: 15px; line-height: 1.35; margin-top: 14px; }
  .contact .lines { list-style: none; margin-top: 16px; font-size: 15px; }
  .contact .lines li { display: flex; align-items: center; gap: 10px; margin-bottom: 6px; white-space: nowrap; }
  .contact .lines svg { width: 14px; height: 14px; flex: none; }
  .front-band {
    position: absolute; left: 0; right: 0; bottom: 0; height: 12px;
    background: linear-gradient(90deg, var(--brand-purple), var(--brand-blue) 35%, var(--brand-red) 65%, var(--brand-orange) 85%, var(--brand-yellow));
  }
  .front-edge {
    position: absolute; top: 0; bottom: 0; right: 0; width: 8px;
    background: linear-gradient(180deg, var(--brand-yellow), var(--brand-orange));
  }
</style>
</head>
<body>

  <section class="card card-back" aria-label="Business card back">
    <div class="brand-lockup">
      <span class="brand-mark"></span>
      <p class="brand-name">Covenant<br>Elders<br>Assembly<br>of Harvest<br>Fellowship</p>
    </div>
    <div class="edge-band"></div>
  </section>

  <section class="card card-front" aria-label="Business card front">
    <div class="brand-lockup">
      <span class="brand-mark"></span>
      <p class="brand-name">Covenant<br>Elders<br>Assembly<br>of Harvest<br>Fellowship</p>
    </div>
    <div class="divider"></div>
    <div class="contact">
      <p class="name">Rev. Tobias Okonkwe</p>
      <p class="role">Convener/Chairman Board of Trustees</p>
      <p class="address">14 Rimi Kasa Street, off Gwagwa - Karu Link Road,<br>Nyanya Abuja, FCT, Nigeria</p>
      <ul class="lines">
        <li><svg viewBox="0 0 16 16"><path fill="#2f5fb3" d="M4 1h3l1 4-2 1a9 9 0 0 0 4 4l1-2 4 1v3c0 1-1 2-2 2A13 13 0 0 1 1 3c0-1 1-2 3-2z"/></svg>+234 800 555 0142</li>
        <li><svg viewBox="0 0 16 16"><path fill="#e2452b" d="M4 1h3l1 4-2 1a9 9 0 0 0 4 4l1-2 4 1v3c0 1-1 2-2 2A13 13 0 0 1 1 3c0-1 1-2 3-2z"/></svg>+234 800 555 0187</li>
        <li><svg viewBox="0 0 16 16"><rect x="1" y="3" width="14" height="10" fill="none" stroke="#f08a1c" stroke-width="1.6"/><path d="M1 3l7 6 7-6" fill="none" stroke="#f08a1c" stroke-width="1.6"/></svg>covenant.elders.assembly@mailvale.example</li>
        <li><svg viewBox="0 0 16 16"><circle cx="8" cy="8" r="6.5" fill="none" stroke="#f5b51c" stroke-width="1.6"/><path d="M1.5 8h13M8 1.5c-3 3.5-3 9.5 0 13M8 1.5c3 3.5 3 9.5 0 13" fill="none" stroke="#f5b51c" stroke-width="1.2"/></svg>www.covenantelders.example</li>
      </ul>
    </div>
    <div class="front-edge"></div>
    <div class="front-band"></div>
  </section>

</body>
</html>
```